Brivora Collective Business Card Design

We need a business card design for Brivora Collective. We are a healthcare recruiting, wellness and education company. We partner with medical facilities to find quality candidates. We also offer free wellness courses.
The final design should communicate an emphasis on recruiting and wellness
The main purpose of the business card is to utilized it for networking events, give to hospitals, executives, VCs surgery centers and clinics. I want it to be sleek, clean, use of our brand colors and professional.

```html
<!DOCTYPE html>
<html lang="en">
<head>
<meta charset="utf-8">
<title>Brivora Collective Business Card</title>
<link rel="stylesheet" href="https://fonts.googleapis.com/css2?family=Roboto:wght@400;500&family=Source+Serif+4:wght@400&display=swap">
<style>
  :root {
    --backdrop: #9b9b9b;
    --paper: #f7f7f5;
    --brand-green: #12645a;
    --card-green: #03574c;
    --card-green-mark: #0f6b5e;
    --ink-grey: #5f6261;
    --card-shadow: rgba(0, 0, 0, 0.28);
  }
  * { margin: 0; padding: 0; box-sizing: border-box; }
  html, body {
    width: 1200px;
    height: 1083px;
    overflow: hidden;
    background: var(--backdrop);
  }
  .stage {
    position: relative;
    width: 1200px;
    height: 1083px;
    display: flex;
    flex-direction: column;
    align-items: center;
    justify-content: center;
    gap: 60px;
  }
  .card {
    position: relative;
    width: 630px;
    height: 360px;
    box-shadow: 0 14px 34px var(--card-shadow);
  }
  .card--front { background: var(--paper); }
  .card--back {
    background: var(--card-green);
    display: flex;
    align-items: center;
    justify-content: center;
  }
  .person {
    position: absolute;
    left: 46px;
    top: 44px;
  }
  .person__name {
    font-family: "Source Serif 4", Georgia, serif;
    font-size: 24px;
    font-weight: 400;
    color: var(--brand-green);
    letter-spacing: 0.2px;
  }
  .person__role {
    font-family: "Roboto", Arial, sans-serif;
    font-size: 15px;
    color: var(--ink-grey);
    margin-top: 2px;
  }
  .contact {
    position: absolute;
    left: 46px;
    bottom: 46px;
    list-style: none;
    font-family: "Roboto", Arial, sans-serif;
    font-size: 13.5px;
    color: var(--ink-grey);
    line-height: 20px;
  }
  .contact__item {
    display: flex;
    align-items: center;
    gap: 8px;
  }
  .contact__icon {
    width: 14px;
    height: 14px;
    fill: var(--brand-green);
    flex: none;
  }
  .brand {
    position: absolute;
    right: 48px;
    top: 130px;
    display: flex;
    align-items: center;
    gap: 12px;
  }
  .brand__square {
    width: 30px;
    height: 30px;
    border-radius: 5px;
    background: var(--brand-green);
  }
  .brand__name {
    font-family: "Roboto", Arial, sans-serif;
    font-weight: 500;
    font-size: 27px;
    color: var(--brand-green);
  }
  .brand--back { position: static; gap: 16px; }
  .brand--back .brand__square {
    width: 42px;
    height: 42px;
    background: var(--card-green-mark);
  }
  .brand--back .brand__name {
    font-size: 38px;
    color: var(--card-green-mark);
  }
</style>
</head>
<body>
<main class="stage">
  <section class="card card--front" aria-label="Card front">
    <div class="person">
      <h1 class="person__name">Maren Holloway</h1>
      <p class="person__role">Founder &amp; CEO</p>
    </div>

    <div class="brand">
      <span class="brand__square"></span>
      <span class="brand__name">Brivora Collective</span>
    </div>

    <ul class="contact">
      <li class="contact__item">
        <svg class="contact__icon" viewBox="0 0 24 24"><path d="M6.6 10.8a15.1 15.1 0 0 0 6.6 6.6l2.2-2.2c.3-.3.7-.4 1-.2 1.1.4 2.3.6 3.6.6.6 0 1 .4 1 1V20c0 .6-.4 1-1 1A17 17 0 0 1 3 4c0-.6.4-1 1-1h3.5c.6 0 1 .4 1 1 0 1.3.2 2.5.6 3.6.1.3 0 .7-.2 1z"/></svg>
        (555) 014-2290
      </li>
      <li class="contact__item">
        <svg class="contact__icon" viewBox="0 0 24 24"><path d="M2 5h20v14H2zm2 2v.4l8 5.1 8-5.1V7zm16 2.8-8 5.1-8-5.1V17h16z"/></svg>
        info@brivoracollective.com
      </li>
      <li class="contact__item">
        <svg class="contact__icon" viewBox="0 0 24 24"><path d="M12 2a10 10 0 1 0 0 20 10 10 0 0 0 0-20zm6.9 6h-3a15.6 15.6 0 0 0-1.3-3.9A8 8 0 0 1 18.9 8zM12 4c.8 1.2 1.5 2.5 1.9 4h-3.8c.4-1.5 1.1-2.8 1.9-4zM4.3 14a8 8 0 0 1 0-4h3.4a16 16 0 0 0 0 4zm.8 2h3a15.6 15.6 0 0 0 1.3 3.9A8 8 0 0 1 5.1 16zm3-8h-3a8 8 0 0 1 4.3-3.9C8.8 5.3 8.4 6.6 8.1 8zM12 20c-.8-1.2-1.5-2.5-1.9-4h3.8c-.4 1.5-1.1 2.8-1.9 4zm2.3-6H9.7a14 14 0 0 1 0-4h4.6a14 14 0 0 1 0 4zm.3 5.9c.6-1.2 1-2.5 1.3-3.9h3a8 8 0 0 1-4.3 3.9zm1.7-5.9a16 16 0 0 0 0-4h3.4a8 8 0 0 1 0 4z"/></svg>
        info@brivoracollective.com
      </li>
      <li class="contact__item">
        <svg class="contact__icon" viewBox="0 0 24 24"><path d="M12 2a7 7 0 0 0-7 7c0 5.2 7 13 7 13s7-7.8 7-13a7 7 0 0 0-7-7zm0 9.5a2.5 2.5 0 1 1 0-5 2.5 2.5 0 0 1 0 5z"/></svg>
        42 Fenwick Road Ashby - AB1 2CD
      </li>
    </ul>
  </section>

  <section class="card card--back" aria-label="Card back">
    <div class="brand brand--back">
      <span class="brand__square"></span>
      <span class="brand__name">Brivora Collective</span>
    </div>
  </section>
</main>
</body>
</html>
```